Brennick Holdings Business Cards

These are professional business cards that are for my family office.
Put fake emails and phone numbers as of now until I finalize those components. This family office controls my families investments, assets, and future. The cards should be professional.
..
.
.
.
I just uploaded another variation of a logo I would like to see as a business card to I am inbeteen which logo to use

Target Market(s)

business

Industry/Entity Type

business

Contact Information for Business Card

Professional, wealth related, finance related.

Requirements
Must have
• Logo

```html
<!DOCTYPE html>
<html lang="en">
<head>
<meta charset="utf-8">
<title>Brennick Holdings Business Cards</title>
<link href="https://fonts.googleapis.com/css2?family=Cinzel:wght@400&family=Montserrat:wght@400;700&display=swap" rel="stylesheet">
<style>
  :root {
    --bg: #e9e9e9;
    --card-white: #ffffff;
    --card-black: #0b0b0b;
    --ink: #111111;
    --ink-soft: #2a2a2a;
    --paper: #ffffff;
  }
  * { margin: 0; padding: 0; box-sizing: border-box; }
  html, body {
    width: 1200px; height: 801px; overflow: hidden;
    background: var(--bg);
  }
  .stage {
    position: relative; width: 1200px; height: 801px;
    display: flex; align-items: center; justify-content: center; gap: 60px;
  }
  .card {
    position: relative; width: 525px; height: 300px;
    box-shadow: 0 6px 18px rgba(0,0,0,0.18);
  }
  .card--front { background: var(--card-white); color: var(--ink); }
  .card--back { background: var(--card-black); color: var(--paper); display: flex; align-items: center; justify-content: center; }

  .brand {
    position: absolute; top: 42px; right: 40px;
    display: flex; flex-direction: column; align-items: center; gap: 14px;
  }
  .brand__dot {
    width: 58px; height: 58px; border-radius: 50%;
    border: 3px solid var(--ink);
  }
  .brand__name {
    font-family: "Cinzel", serif; font-size: 19px; letter-spacing: 1px;
    color: var(--ink);
  }

  .person {
    position: absolute; left: 36px; top: 128px; right: 0;
    display: flex; align-items: flex-end; gap: 14px;
  }
  .person__text { font-family: "Montserrat", sans-serif; white-space: nowrap; }
  .person__name { font-weight: 700; font-size: 19px; letter-spacing: 0.5px; line-height: 1.05; }
  .person__role { font-weight: 400; font-size: 13px; color: var(--ink-soft); }
  .person__rule { flex: 1; height: 2px; background: var(--ink); margin-bottom: 20px; }

  .contact {
    position: absolute; left: 36px; top: 196px;
    font-family: "Montserrat", sans-serif; font-size: 13px; color: var(--ink);
    list-style: none; line-height: 1.25;
  }
  .contact li { display: flex; align-items: center; gap: 7px; }
  .contact svg { width: 11px; height: 11px; flex: none; }
  .contact__address { margin-top: 4px; padding-left: 18px; }

  .back-brand { display: flex; align-items: center; gap: 16px; }
  .back-brand__dot { width: 72px; height: 72px; border-radius: 50%; border: 3px solid var(--paper); }
  .back-brand__name { font-family: "Cinzel", serif; font-size: 24px; letter-spacing: 1px; color: var(--paper); }
</style>
</head>
<body>
<main class="stage">
  <section class="card card--front" aria-label="Business card front">
    <div class="brand">
      <span class="brand__dot"></span>
      <span class="brand__name">Brennick Holdings</span>
    </div>

    <div class="person">
      <div class="person__text">
        <p class="person__name">YOUR NAME</p>
        <p class="person__role">Designation</p>
      </div>
      <span class="person__rule"></span>
    </div>

    <ul class="contact">
      <li>
        <svg viewBox="0 0 24 24" aria-hidden="true"><path fill="currentColor" d="M6.6 10.8a15.5 15.5 0 0 0 6.6 6.6l2.2-2.2c.3-.3.7-.4 1-.2 1.1.4 2.3.6 3.6.6.6 0 1 .4 1 1V20c0 .6-.4 1-1 1A17 17 0 0 1 3 4c0-.6.4-1 1-1h3.5c.6 0 1 .4 1 1 0 1.3.2 2.5.6 3.6.1.3 0 .7-.2 1z"/></svg>
        123-456-7890
      </li>
      <li>
        <svg viewBox="0 0 24 24" aria-hidden="true"><rect x="2" y="4" width="20" height="16" fill="currentColor"/><path d="M3 5l9 7 9-7" fill="none" stroke="#fff" stroke-width="2"/></svg>
        example@mail.com
      </li>
      <li>
        <svg viewBox="0 0 24 24" aria-hidden="true"><circle cx="12" cy="12" r="10" fill="currentColor"/><path d="M2 12h20M12 2c3 3 3 17 0 20M12 2c-3 3-3 17 0 20" fill="none" stroke="#fff" stroke-width="1.5"/></svg>
        www.example.com
      </li>
      <li class="contact__address">No.00, Street, City,<br>State, Zip Code</li>
    </ul>
  </section>

  <section class="card card--back" aria-label="Business card back">
    <div class="back-brand">
      <span class="back-brand__dot"></span>
      <span class="back-brand__name">Brennick Holdings</span>
    </div>
  </section>
</main>
</body>
</html>
```